Business cards to launch an education platform

Hi,
I am looking at having new business cards designed.
I am a startup, developing a web platform for schools and university, the education world. It's an online assessment system.
I would like a card that looks classy, and that is using the colors and the font of my logo.

I have attached:
1) my logo
2) A business card that I have designed quickly so you can have all the information required in the card, but I really don't like it.
3) The font that I am using (Lato Regular) to design my web platform
4) Some screenshots of my web platform so you can have a look at the style that I have.

Target Market(s)

Major market: Education system: Schools and university
Minor markets: Business in general

Industry/Entity Type

Business

Contact Information for Business Card

Lydia Marsh
Director

M: 0437 681 902
E: lydia.marsh@copperLeafSystems.com.au

Requirements
Must have
• The colors of my logo

```html
<!DOCTYPE html>
<html lang="en">
<head>
<meta charset="utf-8">
<title>Copper Leaf Systems – Business Cards</title>
<link rel="stylesheet" href="https://fonts.googleapis.com/css2?family=EB+Garamond:wght@400;700&family=Lato:wght@400&display=swap">
<style>
  :root {
    --stage: #2a2a2c;
    --blue-deep: #0e6fb8;
    --blue-mid: #2a8fd6;
    --blue-light: #8fcaf0;
    --navy: #17325f;
    --rule-blue: #1f4a9a;
    --ink: #2b2b2e;
    --paper: #f4f4f5;
    --paper-edge: #e2e3e6;
  }
  * { box-sizing: border-box; margin: 0; padding: 0; }
  html, body { width: 1200px; height: 873px; overflow: hidden; }
  body { background: var(--stage); position: relative; }

  .card {
    position: absolute;
    width: 540px;
    height: 310px;
    border-radius: 18px;
    overflow: hidden;
    box-shadow: 0 10px 30px rgba(0,0,0,.45);
  }

  /* Back of card */
  .card-back {
    left: 40px;
    top: 281px;
    background:
      radial-gradient(ellipse 260px 170px at 62% 40%, rgba(200,230,250,.55), transparent 70%),
      linear-gradient(135deg, var(--blue-mid) 0%, var(--blue-deep) 100%);
  }
  .back-brand {
    position: absolute;
    right: 44px;
    top: 112px;
    text-align: right;
  }
  .back-brand .wordmark {
    display: flex;
    align-items: center;
    justify-content: flex-end;
    gap: 12px;
    font-family: "Lato", sans-serif;
    font-size: 34px;
    letter-spacing: 2px;
    color: var(--navy);
  }
  .back-brand .mark {
    width: 22px; height: 22px;
    background: var(--navy);
  }
  .back-brand .rule {
    height: 1px;
    background: var(--navy);
    margin: 12px 0 9px;
    width: 330px;
    margin-left: auto;
  }
  .back-brand .tagline {
    font-family: "Lato", sans-serif;
    font-size: 12px;
    letter-spacing: 3.5px;
    color: var(--navy);
  }

  /* Front of card */
  .card-front {
    left: 620px;
    top: 281px;
    background: linear-gradient(160deg, #ffffff 0%, var(--paper) 60%, var(--paper-edge) 100%);
  }
  .front-brand {
    position: absolute;
    right: 34px;
    top: 34px;
    display: flex;
    align-items: center;
    gap: 10px;
    font-family: "Lato", sans-serif;
    font-size: 24px;
    letter-spacing: 1px;
    color: var(--navy);
  }
  .front-brand .mark {
    width: 30px; height: 30px;
    background: var(--blue-deep);
  }
  .website {
    position: absolute;
    right: 34px;
    top: 124px;
    font-family: "EB Garamond", serif;
    font-size: 12px;
    color: var(--ink);
  }
  .headline-rule {
    position: absolute;
    left: 150px;
    right: 34px;
    top: 143px;
    height: 2px;
    background: var(--rule-blue);
  }
  .person {
    position: absolute;
    left: 30px;
    top: 124px;
  }
  .person .name {
    font-family: "EB Garamond", serif;
    font-weight: 700;
    font-size: 19px;
    color: var(--rule-blue);
  }
  .person .role {
    font-family: "EB Garamond", serif;
    font-size: 13px;
    color: var(--ink);
    margin-top: 2px;
  }
  .contacts {
    position: absolute;
    left: 30px;
    top: 192px;
    list-style: none;
    font-family: "EB Garamond", serif;
    font-size: 13px;
    color: var(--ink);
  }
  .contacts li {
    display: flex;
    align-items: center;
    gap: 12px;
    height: 28px;
  }
  .contacts svg { width: 16px; height: 16px; flex: none; }
</style>
</head>
<body>

  <section class="card card-back" aria-label="Business card back">
    <div class="back-brand">
      <div class="wordmark"><span class="mark"></span>COPPER LEAF SYSTEMS</div>
      <div class="rule"></div>
      <div class="tagline">ONLINE ASSESSMENT SYSTEM</div>
    </div>
  </section>

  <section class="card card-front" aria-label="Business card front">
    <div class="front-brand"><span class="mark"></span>Copper Leaf Systems</div>

    <div class="website">www.copperLeafSystems.com.au</div>
    <div class="headline-rule"></div>

    <div class="person">
      <div class="name">Lydia Marsh</div>
      <div class="role">Director</div>
    </div>

    <ul class="contacts">
      <li>
        <svg viewBox="0 0 16 16" aria-hidden="true"><rect x="4" y="1" width="8" height="14" rx="1.5" fill="none" stroke="#1f4a9a" stroke-width="1.5"/><line x1="7" y1="12.5" x2="9" y2="12.5" stroke="#1f4a9a" stroke-width="1.2"/></svg>
        0437 681 902
      </li>
      <li>
        <svg viewBox="0 0 16 16" aria-hidden="true"><rect x="1" y="3" width="14" height="10" fill="#1f4a9a"/><polyline points="1,3.5 8,9 15,3.5" fill="none" stroke="#fff" stroke-width="1.2"/></svg>
        lydia.marsh@copperLeafSystems.com.au
      </li>
      <li>
        <svg viewBox="0 0 16 16" aria-hidden="true"><path d="M8 1a5 5 0 0 0-5 5c0 4 5 9 5 9s5-5 5-9a5 5 0 0 0-5-5z" fill="#1f4a9a"/><circle cx="8" cy="6" r="1.8" fill="#fff"/></svg>
        PO Box 58 Glebe NSW 2037 AU
      </li>
    </ul>
  </section>

</body>
</html>
```